Ferncrest Dental, LLC business card project

Business card to be designed with current logo.
Dental office- please keep design of card that looks clean and professional.
Please include the following info:
Ferncrest Dental, LLC
Dr. Lorna Pettigrew
2871 Marlowe Street
Bethlehem, PA 18093
610-555-0193
ferncrestdental.office@examplemail.test
Hello everyone-
Reason: Just got back from overseas- will look at all designs and provide feedback. Thank you!
Reason: Polling my friends for the final selection-
thank you to all those that participated- so many talented designers!

```html
<!DOCTYPE html>
<html lang="en">
<head>
<meta charset="utf-8">
<title>Ferncrest Dental, LLC – Business Card</title>
<link rel="stylesheet" href="https://fonts.googleapis.com/css2?family=PT+Sans:wght@400;700&display=swap">
<style>
  :root {
    --backdrop: #232323;
    --charcoal: #3d3d3d;
    --charcoal-deep: #2f2f2f;
    --leaf: #8cc63f;
    --leaf-light: #9bd13f;
    --leaf-deep: #5f9e1a;
    --brand-green: #8fcf2e;
    --ink-soft: #3f5a1c;
    --white: #ffffff;
  }
  * { margin: 0; padding: 0; box-sizing: border-box; }
  html, body {
    width: 1200px; height: 900px; overflow: hidden;
    background: var(--backdrop);
    font-family: "PT Sans", Arial, sans-serif;
  }
  .canvas { position: relative; width: 1200px; height: 900px; }

  .card {
    position: absolute;
    width: 640px; height: 366px;
    border-radius: 4px;
    overflow: hidden;
    box-shadow: 0 14px 30px rgba(0,0,0,.45);
  }

  /* Card front: charcoal with brand name */
  .card-front {
    left: 120px; top: 70px;
    background: linear-gradient(160deg, var(--charcoal) 0%, var(--charcoal-deep) 100%);
    display: flex; align-items: center; justify-content: center;
  }

  .brand {
    display: flex; align-items: center; gap: 12px;
    font-family: "PT Sans", Arial, sans-serif;
    font-weight: 400;
    color: var(--brand-green);
    white-space: nowrap;
  }
  .brand-dot {
    width: 16px; height: 16px; border-radius: 50%;
    background: var(--brand-green);
    flex: none;
  }
  .card-front .brand-name { font-size: 40px; }

  /* Card back: green with contact details */
  .card-back {
    left: 440px; top: 464px;
    background: linear-gradient(165deg, var(--leaf-light) 0%, var(--leaf) 45%, var(--leaf-deep) 100%);
    color: var(--white);
  }

  .holder { position: absolute; left: 40px; top: 52px; }
  .holder-name { font-size: 34px; font-weight: 700; letter-spacing: .5px; line-height: 1; }
  .holder-title { margin-top: 8px; font-size: 16px; color: var(--ink-soft); padding-left: 4px; }

  .brand-band {
    position: absolute;
    left: 360px; top: 70px;
    width: 280px; height: 92px;
    background: var(--charcoal);
    border-radius: 10px 0 0 10px;
    display: flex; align-items: center; padding-left: 22px;
  }
  .brand-band .brand { gap: 9px; }
  .brand-band .brand-dot { width: 11px; height: 11px; }
  .brand-band .brand-name { font-size: 21px; }

  .contact {
    position: absolute; left: 40px; bottom: 34px;
    list-style: none;
    display: flex; flex-direction: column; gap: 12px;
    font-size: 18px;
  }
  .contact-item { display: flex; align-items: flex-start; gap: 14px; line-height: 1.15; }
  .contact-icon { width: 20px; height: 20px; flex: none; margin-top: 1px; }
</style>
</head>
<body>
<main class="canvas">

  <section class="card card-front" aria-label="Card front">
    <div class="brand">
      <span class="brand-dot"></span>
      <span class="brand-name">Ferncrest Dental, LLC</span>
    </div>
  </section>

  <section class="card card-back" aria-label="Card back">
    <div class="holder">
      <h1 class="holder-name">Dr. Lorna Pettigrew</h1>
      <p class="holder-title">Dental Doctor</p>
    </div>

    <div class="brand-band">
      <div class="brand">
        <span class="brand-dot"></span>
        <span class="brand-name">Ferncrest Dental, LLC</span>
      </div>
    </div>

    <ul class="contact">
      <li class="contact-item">
        <svg class="contact-icon" viewBox="0 0 20 20" aria-hidden="true">
          <rect x="5" y="1" width="10" height="18" rx="2" fill="none" stroke="#fff" stroke-width="1.6"/>
          <rect x="7" y="4" width="6" height="6" fill="#fff"/>
          <circle cx="10" cy="15.5" r="1.2" fill="#fff"/>
        </svg>
        <span>610-555-0193</span>
      </li>
      <li class="contact-item">
        <svg class="contact-icon" viewBox="0 0 20 20" aria-hidden="true">
          <rect x="1.5" y="4" width="17" height="12" rx="1" fill="none" stroke="#fff" stroke-width="1.6"/>
          <path d="M2 5 L10 11 L18 5" fill="none" stroke="#fff" stroke-width="1.6"/>
        </svg>
        <span>ferncrestdental.office@examplemail.test</span>
      </li>
      <li class="contact-item">
        <svg class="contact-icon" viewBox="0 0 20 20" aria-hidden="true">
          <path d="M10 1 C6 1 3.5 4 3.5 7.5 C3.5 12 10 19 10 19 C10 19 16.5 12 16.5 7.5 C16.5 4 14 1 10 1 Z" fill="#fff"/>
          <circle cx="10" cy="7.5" r="2.5" fill="var(--leaf)"/>
        </svg>
        <span>2871 Marlowe Street<br>Bethlehem, PA 18093</span>
      </li>
    </ul>
  </section>

</main>
</body>
</html>
```